Business Card Design Project

Hello Designers, hope you are all aiming enjoy the weekend
I have the Business Logo (uploaded), you can alter the color which ever way you think would work,
Im looking for a simple yet striking feel, something which will stay memorable (I have uploaded 3 examples for you to flick through)
Information on the card, will just be the bare minimum,
Double Sided
Info being
i.e.
Name
Number
Website
ABN
Tobin Wexmoor
+468213579 (singapore)
+315792846 (Australia)
+729384615 (America)
www.lomevu-linkup.example
ABN 86420913
Enjoy,
Tobin
Industry/Entity Type
Business
Look and feel
Each slider illustrates characteristics of the customer's brand and the style your logo design should communicate.

```html
<!DOCTYPE html>
<html lang="en">
<head>
<meta charset="utf-8">
<title>Lomevu Linkup Business Card</title>
<link href="https://fonts.googleapis.com/css2?family=Questrial&display=swap" rel="stylesheet">
<style>
  :root {
    --page-bg: #ffffff;
    --card-dark: #404040;
    --card-light: #ffffff;
    --card-border: #1a1a1a;
    --brand-teal: #12919c;
    --brand-grey: #5f5f5f;
    --text-light: #dcdcdc;
    --text-dark: #333333;
  }
  * { margin: 0; padding: 0; box-sizing: border-box; }
  html, body {
    width: 1200px;
    height: 462px;
    overflow: hidden;
    background: var(--page-bg);
    font-family: "Questrial", sans-serif;
  }
  .canvas {
    position: relative;
    width: 1200px;
    height: 462px;
  }
  .card {
    position: absolute;
    top: 73px;
    width: 514px;
    height: 314px;
  }
  .card--front {
    left: 73px;
    background: var(--card-dark);
    border-radius: 22px;
  }
  .card--back {
    left: 601px;
    background: var(--card-light);
    border: 2px solid var(--card-border);
    border-radius: 28px;
  }
  .brand {
    position: absolute;
    display: flex;
    align-items: center;
    white-space: nowrap;
  }
  .brand__mark {
    display: block;
    background: var(--brand-teal);
    border-radius: 8px;
  }
  .brand__name {
    line-height: 1;
  }
  .card--front .brand {
    left: 0;
    right: 0;
    top: 124px;
    justify-content: center;
    gap: 18px;
  }
  .card--front .brand__mark {
    width: 56px;
    height: 56px;
  }
  .card--front .brand__name {
    font-size: 54px;
    color: var(--text-light);
  }
  .front__website {
    position: absolute;
    left: 0;
    right: 0;
    top: 232px;
    text-align: center;
    font-size: 21px;
    color: var(--text-light);
    letter-spacing: 0.2px;
  }
  .card--back .brand {
    left: 13px;
    top: 12px;
    gap: 22px;
  }
  .card--back .brand__mark {
    width: 74px;
    height: 75px;
  }
  .card--back .brand__name {
    font-size: 50px;
    color: var(--brand-grey);
  }
  .contact {
    position: absolute;
    left: 241px;
    top: 114px;
    list-style: none;
    font-size: 19px;
    line-height: 24px;
    color: var(--text-dark);
  }
</style>
</head>
<body>
  <main class="canvas">
    <section class="card card--front" aria-label="Card front">
      <div class="brand">
        <span class="brand__mark" aria-hidden="true"></span>
        <span class="brand__name">Lomevu Linkup</span>
      </div>
      <p class="front__website">www.lomevu-linkup.example</p>
    </section>

    <section class="card card--back" aria-label="Card back">
      <div class="brand">
        <span class="brand__mark" aria-hidden="true"></span>
        <span class="brand__name">Lomevu Linkup</span>
      </div>
      <ul class="contact">
        <li class="contact__name">Tobin Wexmoor</li>
        <li class="contact__phone">+468213579 (singapore)</li>
        <li class="contact__phone">+315792846 (Australia)</li>
        <li class="contact__phone">+729384615 (America)</li>
        <li class="contact__website">www.lomevu-linkup.example</li>
        <li class="contact__abn">ABN 86420913</li>
      </ul>
    </section>
  </main>
</body>
</html>
```